Letterhead and email signature block for school

We are a Remote School in the North West of Western Australia and I want to take our logo and use that to create a professional letter head and email signature block. A sample signature block is attached. For the Letterhead; The logo is also attached. I like the Orange and black combination of the logo, needs to include motto plus the following contact details;
PMB 3 BROOME WA
Phone: (08) 9176 3058
Fax: (08) 9176 3047
ABN: 41 297 580 114

The email signature block needs to have the following;
Devon Lukas Farrow
Principal
Tallowood Creek RCS
Phone: (08) 9176 3058
Fax: (08) 9176 3047
Mobile: 0455 318 207
Email: Devon.Farrow@learnwave.edu.au

Target Market(s)

Parents

Industry/Entity Type

Education

Contact Information for Business Card

Devon Lukas Farrow
Principal
Tallowood Creek RCS
Phone: (08) 9176 3058
Fax: (08) 9176 3047
Mobile: 0455 318 207

Colors
f37122
000000

Requirements
Must have
• see breif

```html
<!DOCTYPE html>
<html lang="en">
<head>
<meta charset="utf-8">
<title>Devon Lukas Farrow – Email Signature</title>
<link rel="stylesheet" href="https://fonts.googleapis.com/css2?family=Mulish:wght@400;600;800&display=swap">
<style>
  :root {
    --orange: #f37122;
    --black: #000000;
    --grey: #9a9a9a;
    --paper: #ffffff;
    --art-dark: #2a2320;
    --art-light: #e9743a;
  }
  * { margin: 0; padding: 0; box-sizing: border-box; }
  html, body {
    width: 1200px;
    height: 583px;
    overflow: hidden;
    background: var(--paper);
    font-family: "Mulish", "Century Gothic", sans-serif;
  }
  .signature {
    position: relative;
    width: 1200px;
    height: 583px;
  }
  .school-mark {
    position: absolute;
    left: 40px;
    top: 40px;
    width: 222px;
  }
  .school-mark__art {
    display: block;
    width: 210px;
    height: 205px;
    margin-left: 6px;
    border-radius: 6px;
    background: radial-gradient(ellipse at 50% 45%, var(--art-light) 0%, #c4581f 45%, var(--art-dark) 100%);
  }
  .school-mark__name {
    margin-top: 10px;
    font-size: 19px;
    font-weight: 600;
    color: var(--black);
    text-align: center;
    white-space: nowrap;
  }
  .divider {
    position: absolute;
    left: 294px;
    top: 65px;
    width: 5px;
    height: 222px;
    background: var(--orange);
  }
  .contact {
    position: absolute;
    left: 337px;
    top: 68px;
    color: var(--black);
  }
  .contact__name {
    font-size: 24px;
    font-weight: 800;
    letter-spacing: 0.5px;
    color: var(--orange);
    text-transform: uppercase;
    line-height: 1.2;
  }
  .contact__role {
    font-size: 17px;
    font-weight: 600;
    letter-spacing: 0.4px;
    line-height: 1.2;
  }
  .contact__lines {
    margin-top: 22px;
    font-size: 16px;
    line-height: 22px;
    white-space: nowrap;
  }
  .contact__label {
    color: var(--orange);
    margin-right: 12px;
  }
  .contact__sep { margin: 0 8px; }
  .social {
    display: flex;
    gap: 9px;
    margin-top: 30px;
  }
  .social__tile {
    width: 30px;
    height: 30px;
    background: var(--orange);
  }
  .disclaimer {
    position: absolute;
    left: 53px;
    top: 316px;
    width: 1112px;
    font-size: 11.6px;
    line-height: 13.5px;
    color: var(--grey);
    text-align: justify;
  }
</style>
</head>
<body>
<main class="signature">
  <section class="school-mark">
    <div class="school-mark__art" role="img" aria-label="School emblem artwork: an orange and black sea eagle catching a fish above blue water"></div>
    <p class="school-mark__name">Tallowood Creek RCS</p>
  </section>

  <div class="divider"></div>

  <section class="contact">
    <h1 class="contact__name">Devon Lukas Farrow</h1>
    <p class="contact__role">Principal</p>
    <div class="contact__lines">
      <p><span class="contact__label">t:</span>(08) 9176 3058<span class="contact__sep">|</span><span class="contact__label">m:</span>0455 318 207<span class="contact__sep">|</span><span class="contact__label">f:</span>(08) 9176 3047</p>
      <p><span class="contact__label">e:</span>Devon.Farrow@learnwave.edu.au<span class="contact__sep">|</span><span class="contact__label">w:</span>www.Devon.Farrow@learnwave.edu.au</p>
    </div>
    <div class="social" aria-label="Social links">
      <span class="social__tile"></span>
      <span class="social__tile"></span>
      <span class="social__tile"></span>
      <span class="social__tile"></span>
    </div>
  </section>

  <p class="disclaimer">Lorem Ipsum is simply dummy text of the printing and typesetting industry. Lorem Ipsum has been the industry's standard dummy text ever since the 1500s, when an unknown printer took a galley of type and scrambled it to make a type specimen book. dummy text ever since the 1500s, when an unknown printer took a galley of type and scrambled it to make a type specimen book. dummy text ever since the 1500s, when an unknown printer took a galley of type and scrambled it to make a type specimen book.</p>
</main>
</body>
</html>
```